Business card design needed

My business is in Matchmaking. My objective is to find the most compatible partner for my clients....basically I'm in the love and happiness industry bringing two people together for a lasting loving relationship.

I envision the design to be something with 2 people who are in love looking happy or even a silhouette.....I don't really know, I'm open to ideas.....maybe no picture at all, but I want it to be classy :-)

I do have a logo which I will upload. You can also go to my website to give you an idea on the colours and the design if that helps, however the website is not finished yet, it should be up by today or tomorrow. If the website has a heart with swirls on the upper left hand corner, that is the old website, please ignore that one. The one that will be up shortly has a picture frame on the home page with my logo that will be in the file I will upload on this page.

Target Market(s)

There are three categories: Over 45, Asian and Western and same sex, but would be able to afford to hire a matchmaker

Contact Information for Business Card

The Tide Lantern
Helping You Find The "One"
Mira Feltham
Matchmaker
0472 915 264
info@thetidelantern.com.au
www.thetidelantern.com.au

```html
<!DOCTYPE html>
<html lang="en">
<head>
<meta charset="utf-8">
<title>The Tide Lantern – Business Card</title>
<link href="https://fonts.googleapis.com/css2?family=Open+Sans:wght@400;700;800&display=swap" rel="stylesheet">
<style>
  :root {
    --backdrop: #e6e6e2;
    --cream: #f4f1cc;
    --plum: #77506f;
    --plum-deep: #6a3f67;
    --teal: #5da69e;
    --ink-light: #f3efc6;
    --photo-dark: #2a2c2b;
    --photo-light: #9a9e9c;
  }
  html, body {
    margin: 0;
    width: 1200px;
    height: 1000px;
    overflow: hidden;
    background: var(--backdrop);
    font-family: "Open Sans", Arial, sans-serif;
  }
  .canvas {
    width: 1200px;
    height: 1000px;
    display: flex;
    align-items: center;
    justify-content: center;
  }
  .business-card {
    position: relative;
    width: 1050px;
    height: 600px;
    display: grid;
    grid-template-columns: 460px 1fr;
    grid-template-rows: 250px 1fr;
    box-shadow: 0 0 0 4px var(--teal), 0 18px 40px rgba(0,0,0,0.25);
    overflow: hidden;
  }
  .card-photo {
    grid-row: 1 / 3;
    grid-column: 1;
    background: radial-gradient(ellipse at 55% 55%, var(--photo-light) 0%, #6c706e 40%, var(--photo-dark) 85%);
  }
  .brand-panel {
    grid-column: 2;
    grid-row: 1;
    background: var(--cream);
    display: flex;
    flex-direction: column;
    align-items: center;
    justify-content: center;
    gap: 14px;
  }
  .brand-name {
    display: flex;
    align-items: center;
    gap: 14px;
    font-size: 46px;
    font-weight: 400;
    color: var(--plum-deep);
    line-height: 1;
  }
  .brand-dot {
    width: 30px;
    height: 30px;
    border-radius: 50%;
    background: var(--teal);
  }
  .brand-tagline {
    font-size: 30px;
    font-weight: 800;
    color: var(--plum-deep);
    letter-spacing: -0.5px;
  }
  .contact-panel {
    grid-column: 2;
    grid-row: 2;
    background: var(--plum);
    color: var(--ink-light);
    padding: 30px 40px;
    display: flex;
    flex-direction: column;
  }
  .person-name {
    font-size: 44px;
    font-weight: 800;
    line-height: 1.05;
  }
  .person-role {
    font-size: 30px;
    font-weight: 700;
    margin-bottom: 26px;
  }
  .contact-line {
    font-size: 30px;
    font-weight: 700;
    line-height: 1.2;
  }
</style>
</head>
<body>
  <main class="canvas">
    <article class="business-card">
      <div class="card-photo" role="img" aria-label="Black and white photograph of two clasped hands, one wearing a diamond engagement ring"></div>
      <header class="brand-panel">
        <div class="brand-name"><span class="brand-dot"></span>The Tide Lantern</div>
        <div class="brand-tagline">Helping You Find The "One"</div>
      </header>
      <section class="contact-panel">
        <div class="person-name">Mira Feltham</div>
        <div class="person-role">Matchmaker</div>
        <div class="contact-line">Tel. 0472 915 264</div>
        <div class="contact-line">mira@thetidelantern.com.au</div>
        <div class="contact-line">www.thetidelantern.com.au</div>
      </section>
    </article>
  </main>
</body>
</html>
```